Brookmere - a website to encourage people to spend time in nature

I have a squarespace site with some content on it but the squarespace template doesn't completely suit my needs, I keep fiddling with the template but actually I need some professional help to get it looking the way I want and with the right 'mood'.
The website is for "Brookmere" - it will be a blog where I write about the importance of nature for good health. I also want to use the website to market services such as outdoor coaching, retreats and walking workshops.
This has been in my head for a LONG time and I currently only use instagram for micro-blogs but it's time for me to get this moving. I've previously engaged other designers on branding for it but they just didn't get it quite the way that I wanted it and I wasn't completely happy with the results. It's been a process for me as to what I want but in the meantime I just didn't come back to the design aspect of it now. I'm looking for a designer who understands the purpose of the website, the ethos and can help me realise this into a design that's clean, clear and simple.

Please note that I have a domain (brookmere.org) and a lot of content drafted on squarespace already. I have published it with password protection - password is brookmere2020 - it still has some of the original template on it, but does have some content. Don't take it as anything to follow in particular, i am looking for fresh eyes and fresh ideas.

Target Market(s)

There are three main groups that I want to target - people who are suffering from stress and anxiety, people who treat them and parents who want to get their kids outside (thereby preventing stress and anxiety)

Contact Information for Business Card

Helen Corbett
Brookmere
Telephone +44 7942 310587
brookmere@mailpost.net

Logo Text

Brookmere - if that. I have an idea that the logo should have a leaf on it somewhere, or maybe just be a leaf.

Coding

Coded - Design and coding required

Number of Pages Required

5+ page

Font styles to use
Serif
Sans Serif

Colors
add136
33b8a4
34a6d7
3377b5

Requirements
Must have
• Space for lots of images. The ability for me to edit the pages if I need to. Be user friendly. Look beautiful.
• For an idea of the images I use and the content I'm interested in writing about have a look at @brookmere on instagram.
• That pop up about cookies so I am complying with data laws.
Should not have
• Must not be too 'busy' I'd like to avoid too much movement.

```html
<!DOCTYPE html>
<html lang="en">
<head>
<meta charset="utf-8">
<title>Brookmere — The Practice Of Feeling Better By Spending Time In Nature</title>
<link href="https://fonts.googleapis.com/css2?family=Cinzel:wght@500;600;700&family=Cormorant+Garamond:ital,wght@1,400;1,500&family=Lato:ital,wght@1,700&family=Poppins:wght@400;500;600&display=swap" rel="stylesheet">
<style>
:root{
  --blue:#2f6db3;
  --blue-deep:#2e66b0;
  --teal:#2ba88c;
  --ink:#333;
  --muted:#555;
  --white:#fff;
}
*{margin:0;padding:0;box-sizing:border-box}
html,body{width:1200px;height:4789px;overflow:hidden}
body{font-family:'Poppins',sans-serif;color:var(--ink);background:var(--white);position:relative}
.photo{display:block}
.btn-solid{display:inline-block;background:var(--teal);color:var(--white);border-radius:22px;font-size:15px;font-weight:500;text-align:center}
.btn-outline{display:inline-block;border:2px solid var(--teal);color:var(--teal);border-radius:20px;font-size:14px;font-weight:500;width:122px;height:38px;line-height:34px;text-align:center}
.btn-ghost{display:inline-block;border:2px solid var(--white);color:var(--white);border-radius:20px;font-size:15px;width:124px;height:40px;line-height:36px;text-align:center}
.section-title{font-family:'Cinzel',serif;font-weight:600;color:var(--blue);font-size:30px;text-align:center;letter-spacing:1px}

.hero{position:absolute;top:0;left:0;width:1200px;height:604px;background:linear-gradient(100deg,#1e2c12 0%,#40601f 30%,#6f8f36 50%,#3f5f1d 70%,#1c2a10 100%)}
.nav{position:absolute;top:62px;right:96px;display:flex;gap:38px;font-size:14px;color:var(--white);letter-spacing:.5px}
.nav span{text-transform:uppercase}
.hero-title{position:absolute;top:228px;width:100%;text-align:center;font-family:'Cinzel',serif;font-weight:600;font-size:58px;color:var(--white);letter-spacing:1px}
.hero-sub{position:absolute;top:300px;width:100%;text-align:center;font-family:'Lato',sans-serif;font-style:italic;font-weight:700;font-size:20px;line-height:28px;color:var(--white)}
.hero .btn-solid{position:absolute;top:377px;left:539px;width:122px;height:44px;line-height:44px}

.blog{position:absolute;top:604px;left:0;width:1200px;height:642px}
.blog .section-title{margin-top:56px}
.cards{position:absolute;left:111px;display:flex;gap:32px}
.card{width:305px}
.card .photo{width:305px;height:223px}
.card h3{color:var(--blue);font-weight:600;font-size:19px;line-height:28px;margin-top:20px}
.card p{font-size:13px;line-height:28px;color:var(--muted);margin-top:10px;margin-bottom:14px}
.blog .cards{top:137px}

.about{position:absolute;top:1246px;left:0;width:1200px;height:394px;background:linear-gradient(160deg,#2b4c74 0%,#1d3656 50%,#2a4a70 100%)}
.about-text{position:absolute;right:115px;top:64px;width:452px;text-align:right;color:var(--white)}
.about-text h2{font-family:'Cinzel',serif;font-weight:600;font-size:30px;letter-spacing:1px}
.about-text p{font-size:13px;line-height:28px;margin-top:8px}
.about-text .btn-ghost{margin-top:30px}

.activities{position:absolute;top:1640px;left:0;width:1200px;height:635px}
.activities .section-title{margin-top:50px}
.activities .cards{top:122px}
.activities .card h3{font-size:26px;margin-top:22px}
.activities .card p{margin-top:6px}

.contact{position:absolute;top:2275px;left:0;width:1200px;height:377px;background:linear-gradient(90deg,#7a7f6e 0%,#5d6446 45%,#4c456c 75%,#35432c 100%)}
.contact h2{font-family:'Cinzel',serif;font-weight:600;font-size:30px;color:var(--white);text-align:center;margin-top:76px;letter-spacing:1px}
.contact p{width:584px;margin:6px auto 0;text-align:center;color:var(--white);font-size:15px;line-height:29px}
.contact .btn-ghost{position:absolute;left:539px;top:257px}

.quote{position:absolute;top:2652px;left:0;width:1200px;height:356px;text-align:center}
.quote blockquote{font-family:'Cormorant Garamond',serif;font-style:italic;font-size:38px;line-height:54px;color:#333;width:790px;margin:76px auto 0}
.quote cite{display:block;font-family:'Cormorant Garamond',serif;font-style:italic;font-size:21px;margin-top:26px;color:#333}

.gallery .photo{position:absolute}

.footer{position:absolute;top:4245px;left:0;width:1200px;height:544px;background:var(--blue-deep);color:var(--white)}
.footer h4{font-size:19px;font-weight:600;text-transform:uppercase;margin-bottom:20px}
.f-col{position:absolute;top:64px}
.f-contact{left:111px}
.f-news{left:412px;width:310px}
.f-links{left:764px}
.f-hours{left:929px}
.f-row{display:flex;gap:16px;font-size:15px;line-height:24px;margin-bottom:18px}
.f-row svg{flex:none;margin-top:4px}
.f-news p,.f-links li,.f-hours li{font-size:14px;line-height:29px}
.f-news p{line-height:22px}
.f-links ul,.f-hours ul{list-style:none}
.email-field{margin-top:18px;width:294px;height:40px;border-radius:20px;background:var(--white);color:#555;font-size:11px;line-height:40px;padding-left:16px}
.f-news .btn-solid{margin-top:16px;width:148px;height:42px;line-height:42px;font-size:15px;font-weight:600}
.f-bottom{position:absolute;top:375px;left:0;width:1200px;border-top:1px solid rgba(255,255,255,.15);text-align:center;font-size:14px;padding-top:35px}
.socials{position:absolute;top:460px;left:540px;display:flex;gap:6px}
.socials span{width:30px;height:30px;border:1.5px solid var(--white);border-radius:50%;background:rgba(255,255,255,.12)}
</style>
</head>
<body>

<header class="hero" role="img" aria-label="Sunlit woodland path through green forest">
  <nav class="nav"><span>Home</span><span>About ⌄</span><span>Blog</span><span>Gallery</span><span>Contact</span></nav>
  <h1 class="hero-title">BROOKMERE</h1>
  <p class="hero-sub">The Practice Of Feeling Better By Spending<br>Time In Nature.</p>
  <span class="btn-solid">Our Story</span>
</header>

<section class="blog">
  <h2 class="section-title">LATEST BLOG</h2>
  <div class="cards">
    <article class="card">
      <div class="photo" role="img" aria-label="Swimmers in a dark forest river" style="background:linear-gradient(180deg,#3b4256,#1c232e 55%,#3d3126)"></div>
      <h3>Why being outside is good for the planet</h3>
      <p>Lorem ipsum dolor sit amet, consectetur adipiscing elit, sed do eiusmod tempor incididunt ut labore et dolore</p>
      <span class="btn-outline">Learn More</span>
    </article>
    <article class="card">
      <div class="photo" role="img" aria-label="Child walking along a country path under a cloudy sky" style="background:linear-gradient(180deg,#d2d4dc,#a3a6b3 48%,#6e6c43 72%,#8c7b51)"></div>
      <h3>Lorem ipsum dolor sit aelit, sdo eiusmod tempor</h3>
      <p>Lorem ipsum dolor sit amet, consectetur adipiscing elit, sed do eiusmod tempor incididunt ut labore et dolore</p>
      <span class="btn-outline">Learn More</span>
    </article>
    <article class="card">
      <div class="photo" role="img" aria-label="Person among a meadow of wildflowers" style="background:linear-gradient(180deg,#7f93b3,#b3bdcc 32%,#4c7a35 52%,#6a4a2c 80%,#3b5e2a)"></div>
      <h3>Lorem ipsum dolor sit aelit, sdo eiusmod tempor</h3>
      <p>Lorem ipsum dolor sit amet, consectetur adipiscing elit, sed do eiusmod tempor incididunt ut labore et dolore</p>
      <span class="btn-outline">Learn More</span>
    </article>
  </div>
</section>

<section class="about" role="img" aria-label="Swimmer in open dark blue water">
  <div class="about-text">
    <h2>ABOUT &nbsp;BROOKMERE</h2>
    <p>Brookmere springs from a simple concept — the idea that spending time in nature is good for you. We don't do enough of it and we should do more if we want to be happier and healthier inhabitants of Planet Earth. Our mission is to get people of all ages outdoors as a means to feel better..</p>
    <span class="btn-ghost">Learn More</span>
  </div>
</section>

<section class="activities">
  <h2 class="section-title">ACTIVITIES</h2>
  <div class="cards">
    <article class="card">
      <div class="photo" role="img" aria-label="Two people walking on a beach at sunset" style="background:linear-gradient(180deg,#5d6b86,#e0b892 38%,#8a8fa0 55%,#c9a98a 75%,#3f4a5e)"></div>
      <h3>Walk</h3>
      <p>Lorem ipsum dolor sit amet, consectetur adipiscing elit, sed do eiusmod tempor incididunt ut labore et dolore</p>
      <span class="btn-outline">Learn More</span>
    </article>
    <article class="card">
      <div class="photo" role="img" aria-label="Coach standing in the sea with a swimmer" style="background:linear-gradient(180deg,#8ab2c4,#4f8ea8 40%,#2f6f8a)"></div>
      <h3>Coach</h3>
      <p>Lorem ipsum dolor sit amet, consectetur adipiscing elit, sed do eiusmod tempor incididunt ut labore et dolore</p>
      <span class="btn-outline">Learn More</span>
    </article>
    <article class="card">
      <div class="photo" role="img" aria-label="Steps leading down into a clear turquoise sea pool" style="background:linear-gradient(180deg,#e4f2f3,#86cfd9 30%,#49aabd 70%,#4f6d49)"></div>
      <h3>Retreat</h3>
      <p>Lorem ipsum dolor sit amet, consectetur adipiscing elit, sed do eiusmod tempor incididunt ut labore et dolore</p>
      <span class="btn-outline">Learn More</span>
    </article>
  </div>
</section>

<section class="contact" role="img" aria-label="Fallen tree among bluebells in a woodland">
  <h2>CONTACT</h2>
  <p>Lorem ipsum dolor sit amet, consectetur adipiscing elit, sed do eiusmod tempor incididunt ut labore et dolore magna aliqua. Quis ipsum suspendisse ultrices gravida. Risus commodo viverra maecenas accumsan lacus vel facilisis.</p>
  <span class="btn-ghost">Inquire</span>
</section>

<section class="quote">
  <blockquote>Nam libero tempore, cum soluta nobis est eligendi optio cumque nihil impedit quo minus id quod maxime placeat facere possimus</blockquote>
  <cite>— Blandit Lectus</cite>
</section>

<section class="gallery">
  <div class="photo" role="img" aria-label="Dog on a dark sandy beach under a blue sky" style="left:0;top:3008px;width:771px;height:827px;background:linear-gradient(180deg,#3b6fcb 0%,#6f98d9 36%,#9ab4d8 39%,#3d3c39 44%,#2a2a27 100%)"></div>
  <div class="photo" role="img" aria-label="Child looking out to sea" style="left:771px;top:3008px;width:429px;height:414px;background:linear-gradient(180deg,#a9c8ea,#7b9cc2 65%,#58595a)"></div>
  <div class="photo" role="img" aria-label="Forest track between tall trees" style="left:771px;top:3422px;width:429px;height:413px;background:linear-gradient(180deg,#3c4a2a,#4f5a36 40%,#6b5a72 75%,#4b4f32)"></div>
  <div class="photo" role="img" aria-label="Ladybird on a green leaf" style="left:0;top:3835px;width:600px;height:410px;background:linear-gradient(135deg,#5b8a4a,#2f5a2c 45%,#1c331c 80%,#2f4a28)"></div>
  <div class="photo" role="img" aria-label="Person on a grassy woodland path" style="left:600px;top:3835px;width:600px;height:410px;background:linear-gradient(180deg,#1d2a15,#34561f 45%,#6a9a34 80%,#4f7a28)"></div>
</section>

<footer class="footer">
  <div class="f-col f-contact">
    <h4>Contact Us</h4>
    <div class="f-row"><svg width="20" height="24" viewBox="0 0 20 24"><path d="M10 0C4.5 0 1 4 1 9c0 6 9 15 9 15s9-9 9-15c0-5-3.5-9-9-9z" fill="#fff"/><circle cx="10" cy="9" r="3.4" fill="#2e66b0"/></svg><div>Brookmere<br>18 Alder Lane<br>Fernhill, NY 12990</div></div>
    <div class="f-row"><svg width="20" height="20" viewBox="0 0 24 24"><path d="M6.6 10.8a15 15 0 0 0 6.6 6.6l2.2-2.2a1 1 0 0 1 1-.25 11.4 11.4 0 0 0 3.6.57 1 1 0 0 1 1 1V20a1 1 0 0 1-1 1A17 17 0 0 1 3 4a1 1 0 0 1 1-1h3.5a1 1 0 0 1 1 1c0 1.25.2 2.45.57 3.57a1 1 0 0 1-.25 1z" fill="#fff"/></svg><div>Phone:<br>(555)-4120-7731</div></div>
    <div class="f-row"><svg width="20" height="20" viewBox="0 0 20 20"><path d="M10 1 1 7v12h18V7z" fill="#fff"/><path d="M2 8l8 6 8-6" fill="none" stroke="#2e66b0" stroke-width="1.5"/></svg><div>Email:<br>info@brookmere.org</div></div>
  </div>
  <div class="f-col f-news">
    <h4>Sign Up For Newsletter</h4>
    <p>excepteur sint occaecat cupidatat non proident, sunt in culpa qui officia deserunt</p>
    <div class="email-field">Enter email</div>
    <span class="btn-solid">SUBSCRIBE</span>
  </div>
  <div class="f-col f-links">
    <h4>Quick Links</h4>
    <ul><li>Home</li><li>About</li><li>Blog</li><li>Gallery</li><li>Contact</li></ul>
  </div>
  <div class="f-col f-hours">
    <h4>Hours</h4>
    <ul><li>Monday — Thursday</li><li>8am — 11pm</li><li>Friday — Sunday</li><li>11am — 11pm</li></ul>
  </div>
  <div class="f-bottom">Brookmere © 2020 All Rights Reserved | Privacy Policy | Terms and Conditions</div>
  <div class="socials" aria-label="Social links"><span aria-label="Social link 1"></span><span aria-label="Social link 2"></span><span aria-label="Social link 3"></span><span aria-label="Social link 4"></span></div>
</footer>

</body>
</html>
```